Roving Kneadery Business Cards

Hi Bogdan,
Thank you for designing my awesome logo! It's awesome. Now I need help in designing my business card. The business card is 3.5" x 2.0". I tried downloading my logo to PressLoom to make my business cards but the design would not fit to scale. Also I would like to have my email included tessa@rovingkneadery-example.com
On the backside of my business card I would like to have a appointment reminder on the back side of my business card
listing a space to record client's name, date, time, of appointment.
Also, I made a car magnet at Press Loom with my logo but I would like to change the width of Roving Kneadery and the sentence When worries stack on worries, you knead to set aside a pause to be the width of the logo space. It's hard to read it on the magnet from a distance. I would also like to include my email address tessa@rovingkneadery-example.com

If it is to hard to fit all of that information in the space maybe I could have the logo as two separate downloads. One with the logo picture, the name of the business, Roving Kneadery and the sentence When worries stack on worries, you knead to set aside a pause. The other download just listing my business name, my phone number, my email address, and services offered. Thanks- Henrietta:)

Reason: Hi Bogdan, I have extended the deadline by 7 days so that you do not feel rushed to get the business card project done by Wednesday. The changes that I need done are: 1. Please enlarge the sentence to be the width of the business card. The Roving Kneadery does not to be the width of the business card just the sentence. 2. The curve on the business card if you can change that curve to sky blue and not black. 3. Change the words phone, email, web address, to just icons of a phone, envelope, and the web symbol. 4. Also put my phone, email, web address on the back of my business card. Thanks, Henrietta

```html
<!DOCTYPE html>
<html lang="en">
<head>
<meta charset="utf-8">
<title>Roving Kneadery Business Card</title>
<link rel="stylesheet" href="https://fonts.googleapis.com/css2?family=Arimo:wght@400;700&family=Archivo+Black&family=Lato:wght@400;700&display=swap">
<style>
  :root {
    --backdrop: #8e8e8e;
    --card-white: #f7f7f5;
    --band-dark: #2f2f2f;
    --accent-orange: #e8921e;
    --ink: #1d1d1d;
    --ink-soft: #4a4a4a;
    --ink-light: #e6e6e6;
    --logo-tone: #d98a2b;
  }
  * { box-sizing: border-box; margin: 0; padding: 0; }
  html, body { width: 1200px; height: 1200px; overflow: hidden; }
  body {
    background: var(--backdrop);
    position: relative;
    font-family: "Lato", sans-serif;
  }
  .card {
    position: absolute;
    left: 250px;
    width: 700px;
    height: 400px;
    background: var(--card-white);
    box-shadow: 0 6px 18px rgba(0,0,0,0.25);
    overflow: hidden;
  }

  /* Back side: appointment reminder */
  .card-back { top: 140px; }
  .reminder-list {
    position: absolute;
    left: 70px; right: 60px; top: 56px;
  }
  .reminder-row {
    display: flex;
    align-items: flex-end;
    height: 28px;
    margin-bottom: 22px;
    font-family: "Archivo Black", sans-serif;
    font-size: 21px;
    line-height: 28px;
    color: var(--ink);
    letter-spacing: 0.5px;
  }
  .reminder-row .label { flex: none; }
  .reminder-row .dots {
    flex: 1;
    margin-left: 6px;
    margin-bottom: 6px;
    border-bottom: 4px dotted var(--ink);
  }
  .back-contacts {
    position: absolute;
    left: 70px; top: 262px;
    list-style: none;
    color: var(--ink-soft);
    font-size: 16px;
    line-height: 20px;
  }
  .back-contacts li { display: flex; align-items: center; margin-bottom: 10px; }
  .back-contacts svg { width: 20px; height: 20px; margin-right: 12px; flex: none; }

  /* Front side */
  .card-front { top: 620px; }
  .logo-art {
    position: absolute;
    left: 80px;
    top: 18px;
    width: 110px;
    height: 120px;
    border-radius: 6px;
    background: linear-gradient(160deg, #c9a6a0 0%, var(--logo-tone) 60%, #b86a1a 100%);
  }
  .business-name {
    position: absolute;
    right: 40px;
    top: 62px;
    font-family: "Arimo", sans-serif;
    font-weight: 700;
    font-size: 30px;
    line-height: 34px;
    color: var(--accent-orange);
    letter-spacing: 0.5px;
  }
  .tagline {
    position: absolute;
    right: 40px;
    top: 106px;
    width: 440px;
    text-align: right;
    font-family: "Arimo", sans-serif;
    font-size: 15px;
    line-height: 20px;
    color: var(--ink);
  }
  .contact-band {
    position: absolute;
    left: 0; top: 168px;
    width: 100%; height: 150px;
    background: var(--band-dark);
  }
  .contact-list {
    position: absolute;
    left: 28px; top: 12px;
    list-style: none;
    color: var(--ink-light);
    font-size: 16px;
    line-height: 20px;
  }
  .contact-list li { display: flex; align-items: flex-start; margin-bottom: 4px; }
  .contact-list svg { width: 22px; height: 22px; margin-right: 14px; flex: none; }
  .person {
    position: absolute;
    right: 40px; top: 82px;
    text-align: right;
    color: #ffffff;
  }
  .person-name { font-size: 25px; font-weight: 400; letter-spacing: 0.5px; }
  .person-role { font-size: 15px; margin-top: 2px; color: var(--ink-light); }
  .accent-stripe {
    position: absolute;
    left: 0; top: 324px;
    width: 100%; height: 34px;
    background: var(--accent-orange);
  }
</style>
</head>
<body>

<section class="card card-back" aria-label="Appointment reminder side">
  <div class="reminder-list">
    <div class="reminder-row"><span class="label">NAME :</span><span class="dots"></span></div>
    <div class="reminder-row"><span class="label">DATE:</span><span class="dots"></span></div>
    <div class="reminder-row"><span class="label">TIME:</span><span class="dots"></span></div>
  </div>
  <ul class="back-contacts">
    <li>
      <svg viewBox="0 0 24 24" aria-hidden="true"><path fill="#4a4a4a" d="M6.6 10.8a15 15 0 0 0 6.6 6.6l2.2-2.2c.3-.3.7-.4 1-.2 1.1.4 2.3.6 3.6.6.6 0 1 .4 1 1V20c0 .6-.4 1-1 1A17 17 0 0 1 3 4c0-.6.4-1 1-1h3.5c.6 0 1 .4 1 1 0 1.3.2 2.5.6 3.6.1.3 0 .7-.2 1z"/></svg>
      <span>+ 000 - 1234 - 5678</span>
    </li>
    <li>
      <svg viewBox="0 0 24 24" aria-hidden="true"><g fill="none" stroke="#4a4a4a" stroke-width="1.8"><rect x="3" y="5" width="18" height="14" rx="1.5"/><path d="M3.5 6l8.5 7 8.5-7"/></g></svg>
      <span>tessa@rovingkneadery-example.com</span>
    </li>
    <li>
      <svg viewBox="0 0 24 24" aria-hidden="true"><g fill="none" stroke="#4a4a4a" stroke-width="1.6"><circle cx="12" cy="12" r="9"/><ellipse cx="12" cy="12" rx="4" ry="9"/><path d="M3 12h18M4.5 7.5h15M4.5 16.5h15"/></g></svg>
      <span>rovingkneadery-example.com</span>
    </li>
  </ul>
</section>

<section class="card card-front" aria-label="Business card front">
  <div class="logo-art" role="img" aria-label="Business logo illustration"></div>
  <div class="business-name">ROVING KNEADERY</div>
  <p class="tagline">When worries stack on worries, you knead to set aside a pause</p>

  <div class="contact-band">
    <ul class="contact-list">
      <li>
        <svg viewBox="0 0 24 24" aria-hidden="true"><path fill="#ddd" d="M6.6 10.8a15 15 0 0 0 6.6 6.6l2.2-2.2c.3-.3.7-.4 1-.2 1.1.4 2.3.6 3.6.6.6 0 1 .4 1 1V20c0 .6-.4 1-1 1A17 17 0 0 1 3 4c0-.6.4-1 1-1h3.5c.6 0 1 .4 1 1 0 1.3.2 2.5.6 3.6.1.3 0 .7-.2 1z"/></svg>
        <span>+ 000 - 1234 - 5678<br>+ 000 - 9876 - 5432</span>
      </li>
      <li>
        <svg viewBox="0 0 24 24" aria-hidden="true"><g fill="none" stroke="#ddd" stroke-width="1.6"><circle cx="12" cy="12" r="9"/><ellipse cx="12" cy="12" rx="4" ry="9"/><path d="M3 12h18M4.5 7.5h15M4.5 16.5h15"/></g></svg>
        <span>tessa@rovingkneadery-example.com<br>rovingkneadery-example.com</span>
      </li>
      <li>
        <svg viewBox="0 0 24 24" aria-hidden="true"><path fill="#ddd" d="M12 3 2 12h3v8h5v-5h4v5h5v-8h3z"/></svg>
        <span>418 Linden Row,<br>Maple Falls 54321</span>
      </li>
    </ul>
    <div class="person">
      <div class="person-name">YOURNAME DOE</div>
      <div class="person-role">Graphic &amp; Web Designer</div>
    </div>
  </div>

  <div class="accent-stripe"></div>
</section>

</body>
</html>
```